One page front and back healthcare law brochure

Our small law firm provides legal services to businesses in the health care industry. We would like a single page 8.5x11 front and back brochure that highlights the services we offer. The intent of the brochure is to communicate our professionalism, high work quality, and depth of experience in healthcare law.
Target Market(s)
Doctors, Hospitals, Medical practices, Dental practices, Healthcare clinics, Healthcare tech companies, Healthcare entrepreneurs, Nurses, Med Spas, Pain Management Clinics, Weight Loss Clinics
Industry/Entity Type
Legal, Healthcare
Requirements
Nice to have
- Visually align with https://tovin.law/ and https://tovin.law/health-care/

```html
<!DOCTYPE html>
<html lang="en">
<head>
<meta charset="utf-8">
<title>Tovin Law Group Healthcare Brochure</title>
<link href="https://fonts.googleapis.com/css2?family=Lato:ital,wght@0,300;0,400;0,700;0,900;1,400&display=swap" rel="stylesheet">
<style>
:root{
  --stage:#f5d5d5;
  --paper:#eef7f9;
  --blue:#1466b8;
  --blue-mid:#1b86cc;
  --blue-dark:#0a4c9e;
  --band:#4a9fd8;
  --ink:#222;
  --grey:#555;
  --white:#fff;
}
*{margin:0;padding:0;box-sizing:border-box}
html,body{width:1200px;height:1200px;overflow:hidden}
body{background:var(--stage);font-family:'Lato',sans-serif;position:relative;color:var(--ink)}
.page{position:absolute;top:233px;width:496px;height:701px;background:var(--paper);overflow:hidden}
.page--front{left:75px}
.page--back{left:629px}
.abs{position:absolute}

/* front */
.hero-photo{left:0;top:0;width:496px;height:177px;background:linear-gradient(120deg,#2a5fa8 0%,#8fb6d8 35%,#e4eef5 60%,#c9dced 100%)}
.firm-name{left:16px;top:16px;display:flex;align-items:center;gap:7px;color:var(--white);font-weight:700;font-size:17px;letter-spacing:.4px}
.firm-name__dot{width:12px;height:12px;border-radius:50%;background:var(--white)}
.intro-band{left:0;top:177px;width:496px;height:115px;background:var(--band);border-top:5px solid var(--blue-dark);border-bottom:5px solid var(--blue-dark)}
.intro-band__right{left:200px;top:182px;width:296px;height:105px;background:#3d8fd0}
.intro-text{left:219px;top:192px;width:252px;font-size:9.4px;line-height:12px;color:var(--white)}
.title-box{left:39px;top:150px;width:161px;height:152px;border:2px solid var(--white);border-radius:5px;background:linear-gradient(180deg,#0a8ad0,#0a55a8);color:var(--white);text-align:center;padding-top:11px;font-size:21px;line-height:26px;font-weight:400}
.title-box strong{font-weight:900}
.section-head{left:0;top:308px;width:496px;text-align:center;font-size:13px;font-weight:700;color:var(--blue)}
.service{width:166px}
.service__icon{position:absolute;left:-45px;top:0;width:28px;height:28px;border-radius:6px}
.service h3{font-size:10px;font-weight:400;color:var(--blue);line-height:12px;margin-bottom:6px}
.service p{font-size:8.7px;line-height:11px;color:var(--ink)}
.foot-rule{left:0;bottom:0;width:496px;height:3px;background:linear-gradient(90deg,var(--blue-dark) 64%,var(--band) 64%)}

/* back */
.chevron{left:0;top:0}
.exp-title{left:12px;top:70px;color:var(--white);font-size:21px;line-height:26px;font-weight:300}
.exp-title strong{font-weight:900;display:block}
.photo{border-radius:3px;border:1px solid #c9dde8}
.case{text-align:center;width:140px}
.case h3{font-size:10px;font-weight:400;color:var(--blue-mid);line-height:12px;margin-bottom:7px}
.case h3 b{font-weight:700}
.case p{font-size:8.6px;line-height:11px;color:var(--grey)}
.why-bg{left:0;top:447px;width:496px;height:212px;background:var(--white)}
.why-photo{left:0;top:447px}
.why-title{left:21px;top:504px;color:var(--blue-dark);font-size:21px;line-height:27px;font-weight:300}
.why-name{left:21px;top:572px;width:140px;color:var(--blue-dark);font-size:15px;line-height:18px;font-weight:700}
.reason{font-size:9px;line-height:12px;color:var(--grey);font-style:italic;width:265px}
.reason b{font-style:normal;font-weight:700;color:#3e5fae}
.phone{left:29px;top:670px;color:var(--white);font-size:17px;font-weight:700;display:flex;align-items:center;gap:9px}
.address{left:204px;top:666px;width:292px;text-align:center;font-size:8.7px;font-weight:700;color:var(--white)}
.contacts{left:255px;top:686px;font-size:9.2px;color:var(--white);display:flex;gap:34px}
</style>
</head>
<body>

<section class="page page--front">
  <div class="abs hero-photo" role="img" aria-label="Photo of a hand stamping a document beside a gavel, stethoscope and scales of justice"></div>
  <div class="abs firm-name"><span class="firm-name__dot"></span>Tovin Law Group</div>

  <div class="abs intro-band"></div>
  <div class="abs intro-band__right"></div>
  <p class="abs intro-text">At Tovin Law Group, our dedicated Healthcare Law Practice Group is committed to safeguarding the interests of healthcare businesses like yours. Our team understands the unique challenges of this highly regulated industry. We are experienced in navigating the complexities of healthcare law to protect your business, allowing you to focus on what you do best: delivering exceptional care.</p>
  <h1 class="abs title-box">YOUR<br>TRUSTED<br>PARTNER IN<br><strong>HEALTH CARE<br>LAW</strong></h1>

  <h2 class="abs section-head">PROTECTING &amp; HELPING YOUR BUSINESS GROW</h2>

  <div class="abs service" style="left:76px;top:336px">
    <span class="service__icon" style="background:#7cbf4a"></span>
    <h3>Legal Support for Growth</h3>
    <p>Whether you’re launching a startup or managing an established enterprise, your focus is on growth. However, amidst the hustle and bustle of business, legal planning often takes a back seat. At Tovin Law Group, we understand the importance of safeguarding your business interests while you focus on expansion.</p>
  </div>
  <div class="abs service" style="left:76px;top:460px">
    <span class="service__icon" style="background:#e9a23b"></span>
    <h3>Navigating Legal Complexities</h3>
    <p>Our Healthcare Law practice offers comprehensive support tailored to the unique needs of healthcare businesses. From establishment to compliance, we guide you through the maze of regulations and legal intricacies, ensuring your business operates smoothly and securely.</p>
  </div>
  <div class="abs service" style="left:76px;top:573px">
    <span class="service__icon" style="background:#e47a5a"></span>
    <h3>Strategic Partnership and Deal Expertise</h3>
    <p>Buying or selling a healthcare business? Forming strategic partnerships? These endeavors are rife with potential pitfalls. Our expert negotiators excel in securing favorable terms and navigating complex deals, allowing you to achieve your business objectives with confidence.</p>
  </div>

  <div class="abs service" style="left:301px;top:336px;width:170px">
    <span class="service__icon" style="background:#5a6a7a"></span>
    <h3>Customized Legal Solutions for Every Business</h3>
    <p>Regardless of your business structure—be it a partnership, LLC, or corporation—legal threats and obstacles must be addressed. Our tailored legal solutions are designed to mitigate risks and propel your business forward, no matter its form or size.</p>
  </div>
  <div class="abs service" style="left:301px;top:451px">
    <span class="service__icon" style="background:#e0485a;border-radius:50%"></span>
    <h3>Focused on<br>Your Success</h3>
    <p>At Tovin Law Group, our mission is clear: to protect and support your business growth. With a dedicated team of legal experts, we alleviate the stress of unaddressed legal issues, allowing you to concentrate on what matters most—building your company.</p>
  </div>
  <div class="abs service" style="left:301px;top:565px">
    <span class="service__icon" style="background:#b86a3a"></span>
    <h3>Your Trusted<br>Legal Partner</h3>
    <p>With Tovin Law Group by your side, you have a trusted partner committed to your success. From navigating regulatory landscapes to negotiating deals, we provide the expertise and support you need to thrive in today’s competitive business environment.</p>
  </div>
  <div class="abs foot-rule"></div>
</section>

<section class="page page--back">
  <svg class="abs chevron" width="200" height="280" viewBox="0 0 200 280">
    <defs><linearGradient id="chev" x1="0" y1="0" x2="1" y2="1"><stop offset="0" stop-color="#2f7fcf"/><stop offset="1" stop-color="#5b7fd0"/></linearGradient></defs>
    <polygon points="62,0 80,0 176,111 68,234 60,226 158,111" fill="#a9bce6"/>
    <polygon points="0,0 62,0 158,111 0,270" fill="url(#chev)"/>
  </svg>
  <h2 class="abs exp-title">EXAMPLES<br>OF OUR<strong>EXPERTISE</strong></h2>

  <div class="abs photo" style="left:181px;top:29px;width:134px;height:95px;background:linear-gradient(135deg,#2aa59a,#dfe9ef)" role="img" aria-label="Photo of medical staff holding a stethoscope and tablet"></div>
  <div class="abs photo" style="left:331px;top:29px;width:134px;height:95px;background:linear-gradient(135deg,#e9eef2,#c9d4dc)" role="img" aria-label="Photo of a facial treatment at a med spa"></div>
  <div class="abs photo" style="left:31px;top:243px;width:134px;height:94px;background:linear-gradient(135deg,#7fb3dd,#d8ebf6)" role="img" aria-label="Photo of a hospital operating room with medical equipment"></div>
  <div class="abs photo" style="left:181px;top:243px;width:134px;height:94px;background:linear-gradient(135deg,#1d2a3a,#4a8fc8)" role="img" aria-label="Photo of a tablet displaying an x-ray scan"></div>
  <div class="abs photo" style="left:331px;top:243px;width:134px;height:94px;background:linear-gradient(135deg,#dfe4e8,#f1f3f4)" role="img" aria-label="Photo of a doctor and a happy patient on a scale"></div>

  <div class="abs case" style="left:178px;top:137px"><h3>MEDICAL <b>PRACTICES</b></h3><p>Navigating the intricate landscape of healthcare regulations, regulatory compliance, and business legal issues. We ensure that your practice operates smoothly while avoiding costly legal pitfalls.</p></div>
  <div class="abs case" style="left:328px;top:137px"><h3>MED <b>SPAS</b></h3><p>Guiding med spas through confusing and ever-changing regulations, licensing, and compliance issues while ensuring their operations are legally sound.</p></div>
  <div class="abs case" style="left:28px;top:347px"><h3>MEDICAL DEVICE<br><b>COMPANIES</b></h3><p>Providing counsel on regulatory compliance, intellectual property, product liability, and contracts to help device manufacturers succeed in a competitive marketplace.</p></div>
  <div class="abs case" style="left:178px;top:347px"><h3>MEDICAL SOFTWARE<br><b>COMPANIES</b></h3><p>Addressing the unique legal needs of software companies in healthcare, including data privacy, cybersecurity, and regulatory compliance.</p></div>
  <div class="abs case" style="left:324px;top:347px;width:148px"><h3>WEIGHT LOSS AND PAIN<br><b>MANAGEMENT CLINICS</b></h3><p>Offering guidance and support on compliance, licensing, and patient care and safety to ensure exceptional care while adhering to strict regulatory standards.</p></div>

  <div class="abs why-bg"></div>
  <svg class="abs why-photo" width="210" height="212" viewBox="0 0 210 212" role="img" aria-label="Yellow-toned photo of a city skyline">
    <defs><linearGradient id="city" x1="0" y1="0" x2="0" y2="1"><stop offset="0" stop-color="#f7ef80"/><stop offset="1" stop-color="#d9cf5a"/></linearGradient></defs>
    <polygon points="0,0 164,0 199,212 0,212" fill="url(#city)"/>
    <polyline points="0,40 58,40 58,62" fill="none" stroke="#1a55a8" stroke-width="1.5"/>
    <polyline points="0,170 58,170 58,150" fill="none" stroke="#1a55a8" stroke-width="1.5"/>
  </svg>
  <h2 class="abs why-title">WHY<br>CHOOSE</h2>
  <div class="abs why-name">Tovin Law Group</div>

  <svg class="abs" style="left:150px;top:466px" width="60" height="175" viewBox="0 0 60 175">
    <g fill="#fff" stroke="#1a55a8" stroke-width="2.5">
      <circle cx="18" cy="18" r="15"/><circle cx="24" cy="63" r="15"/><circle cx="31" cy="110" r="15"/><circle cx="38" cy="155" r="15"/>
    </g>
    <circle cx="18" cy="18" r="9" fill="#e0363f"/>
    <path d="M15 18h6M18 15v6" stroke="#fff" stroke-width="2.5"/>
    <circle cx="24" cy="63" r="8" fill="#f1d3b8"/>
    <path d="M27 114l8-8M28 106l6 0 0 6" stroke="#e0363f" stroke-width="2" fill="none"/>
    <rect x="33" y="149" width="10" height="12" fill="#dfeee5" stroke="#3a8a5a" stroke-width="1"/>
  </svg>
  <p class="abs reason" style="left:195px;top:465px"><b>Industry-Focused:</b> Our deep understanding of the healthcare sector enables us to provide tailored legal solutions.</p>
  <p class="abs reason" style="left:201px;top:502px"><b>Experienced Team:</b> Our HIPAA certified attorneys have extensive experience in healthcare law, delivering effective counsel and representation.</p>
  <p class="abs reason" style="left:208px;top:551px"><b>Proactive Approach:</b> We anticipate challenges before they arise, providing strategic advice to safeguard your business.</p>
  <p class="abs reason" style="left:215px;top:600px"><b>Comprehensive Services:</b> From compliance to drafting legal documents to dispute resolution, we offer end-to-end legal support for most healthcare law needs.</p>

  <svg class="abs" style="left:0;top:659px" width="496" height="42" viewBox="0 0 496 42">
    <rect width="496" height="42" fill="#0a4c9e"/>
    <polygon points="200,6 496,6 496,22 206,22" fill="#1b8fd6"/>
  </svg>
  <div class="abs phone">
    <svg width="16" height="16" viewBox="0 0 24 24"><path fill="#fff" d="M6.6 10.8c1.4 2.8 3.8 5.1 6.6 6.6l2.2-2.2c.3-.3.7-.4 1-.2 1.1.4 2.3.6 3.6.6.6 0 1 .4 1 1V20c0 .6-.4 1-1 1C10.6 21 3 13.4 3 4c0-.6.4-1 1-1h3.5c.6 0 1 .4 1 1 0 1.3.2 2.5.6 3.6.1.3 0 .7-.2 1z"/></svg>
    (555) 214-0387
  </div>
  <div class="abs address">1180 Harlow Road, Suite 310, Ashford, NC, 28000</div>
  <div class="abs contacts"><span>info@tovin.law</span><span>www.tovin.law</span></div>
</section>

</body>
</html>
```